VELRO - Business cards

Business card to be created for Commercial sales staff

Target Market(s)

Commercial businesses

Industry/Entity Type

Commercial

Contact Information for Business Card

Look professional. For commercial clients

Colors
ffffff

Requirements
Must have
• - Velro Logo
• - Commercial sales staff as postion
• - room for commerical sales manager role
• - person name and their mobile number
• - Website : velropower.com.au
Nice to have
• White background.
• On back of business card just have the logo no other information
Should not have
• Should only have white background on front of card.

```html
<!DOCTYPE html>
<html lang="en">
<head>
<meta charset="utf-8">
<title>VELRO Business Cards</title>
<link href="https://fonts.googleapis.com/css2?family=Open+Sans:wght@400;600;800&display=swap" rel="stylesheet">
<style>
  :root {
    --backdrop: #3a3a3a;
    --card-white: #ffffff;
    --brand-red: #c30d16;
    --ink-dark: #2b2d33;
    --ink-body: #333333;
  }
  html, body {
    margin: 0;
    padding: 0;
    width: 1200px;
    height: 900px;
    overflow: hidden;
    background: var(--backdrop);
    font-family: "Open Sans", Arial, sans-serif;
  }
  .sheet {
    position: relative;
    width: 1200px;
    height: 900px;
  }
  .card {
    position: absolute;
    top: 307px;
    width: 500px;
    height: 286px;
    border-radius: 22px;
    overflow: hidden;
    box-shadow: 0 10px 24px rgba(0, 0, 0, 0.35);
  }
  .card-front {
    left: 70px;
    background: var(--card-white);
  }
  .card-back {
    left: 630px;
    background: var(--brand-red);
    display: flex;
    align-items: center;
    justify-content: center;
  }
  .contact-list {
    position: absolute;
    top: 30px;
    right: 30px;
    margin: 0;
    padding: 0;
    list-style: none;
    text-align: right;
    font-size: 12px;
    line-height: 18px;
    color: var(--ink-body);
  }
  .contact-list li {
    display: flex;
    justify-content: flex-end;
    align-items: center;
    gap: 6px;
  }
  .contact-list svg {
    width: 10px;
    height: 10px;
    fill: var(--brand-red);
  }
  .person {
    position: absolute;
    left: 34px;
    top: 112px;
  }
  .person-name {
    margin: 0;
    font-size: 15px;
    font-weight: 600;
    letter-spacing: 0.3px;
    color: var(--brand-red);
    text-transform: uppercase;
  }
  .person-role {
    margin: 2px 0 0;
    font-size: 14px;
    color: var(--ink-body);
  }
  .wordmark {
    display: flex;
    align-items: center;
    gap: 14px;
    font-weight: 800;
    letter-spacing: 2px;
    line-height: 1;
  }
  .wordmark-dot {
    width: 26px;
    height: 26px;
    border-radius: 50%;
  }
  .card-front .wordmark {
    position: absolute;
    left: 40px;
    bottom: 44px;
    font-size: 62px;
    color: var(--ink-dark);
  }
  .card-front .wordmark-dot {
    background: var(--brand-red);
  }
  .card-back .wordmark {
    font-size: 56px;
    color: var(--card-white);
  }
  .card-back .wordmark-dot {
    background: var(--card-white);
  }
</style>
</head>
<body>
  <main class="sheet">
    <section class="card card-front" aria-label="Card front">
      <ul class="contact-list">
        <li>+ 61 400 123 456
          <svg viewBox="0 0 10 10" aria-hidden="true"><rect x="2.5" y="0" width="5" height="10" rx="1"/></svg>
        </li>
        <li>hello@velropower.com.au
          <svg viewBox="0 0 10 10" aria-hidden="true"><rect x="0" y="2" width="10" height="6"/></svg>
        </li>
        <li>www.velropower.com.au
          <svg viewBox="0 0 10 10" aria-hidden="true"><circle cx="5" cy="5" r="5"/></svg>
        </li>
      </ul>
      <div class="person">
        <p class="person-name">Dana Whitfield</p>
        <p class="person-role">Commercial Sales</p>
      </div>
      <div class="wordmark">
        <span class="wordmark-dot" aria-hidden="true"></span>
        <span>VELRO</span>
      </div>
    </section>
    <section class="card card-back" aria-label="Card back">
      <div class="wordmark">
        <span class="wordmark-dot" aria-hidden="true"></span>
        <span>VELRO</span>
      </div>
    </section>
  </main>
</body>
</html>
```